Buchcover für rechtliche Unterstützung von Verantwortungsträgern in Druckereien zum Thema Reklamation
Super engagiert , ging auch auf Sonderwünsche ein und hat einen fantastischen Support gegeben.
Zielgruppe
Wir unterstützen deutschlandweit all diejenigen Verantwortungsträger in Druckereien die bei einer späteren Reklamation von Kunden und Liefernatenverträgen den Kopf hinhalten müssen , indem wir mit unserem System die Sinne für 90% aller im Alltag vorkommenden Vertragsfallen schärfen.
Aufgabenstellung
Titel : Rechtzeitig klug handeln
SL : Einige etwas andere Blicke auf Verträge und Versicherungen der Druckindustrie. Eine Pflichtlektüre für Verantwortliche im Vertrieb und Einkauf und QM des Etiketten- ,und Verpackungsdrucks
Zielgruppe sind Verantwortungsträger in Druckereien wie Einkauf , Vertrieb, Qualitätsmanagement , Geschäftsleitung ( Männer und Frauen gleichermaßen ) eher konservativ , technikorientiert
Vielen Dank für die tollen Vorschläge. Meine Idee war aber mich als Experten zu positionieren . Das Buichg soll auch somit einen Wiedererkennungseffekt bilden. Ich habe einbmal amn Wochenende gesammelt und mich einmal selbst am Layout versucht.

```html
<!DOCTYPE html>
<html lang="de">
<head>
<meta charset="utf-8">
<title>Rechtzeitig klug handeln – Buchcover</title>
<link rel="stylesheet" href="https://fonts.googleapis.com/css2?family=Anton&family=Figtree:wght@400;500&family=Roboto:ital,wght@0,300;0,400;1,700&display=swap">
<style>
  :root {
    --bg-dark: #151515;
    --bg-mid: #2c2c2c;
    --spine: #232325;
    --panel: rgba(34, 35, 40, 0.72);
    --accent: #f7b90f;
    --text-light: #f2f2f2;
    --portrait-a: #5a4a44;
    --portrait-b: #1b1a1c;
  }
  * { margin: 0; padding: 0; box-sizing: border-box; }
  html, body { width: 1200px; height: 833px; overflow: hidden; background: var(--bg-dark); }
  .cover {
    position: relative; width: 1200px; height: 833px; overflow: hidden;
    background:
      radial-gradient(ellipse at 30% 40%, rgba(80,80,80,.35), transparent 60%),
      radial-gradient(ellipse at 80% 20%, rgba(70,70,70,.3), transparent 55%),
      linear-gradient(135deg, var(--bg-mid), var(--bg-dark));
    color: var(--text-light);
  }

  /* Back cover */
  .back-panel {
    position: absolute; left: 115px; top: 125px; width: 311px; height: 600px;
    background: var(--panel);
  }
  .author-photo-small {
    position: absolute; left: 77px; top: 98px; width: 131px; height: 162px;
    background: linear-gradient(180deg, #9a9a9a 0%, #6d6d6d 45%, #1e1e20 100%);
  }
  .brand {
    position: absolute; left: 219px; top: 226px;
    display: flex; align-items: center; gap: 6px;
    font-family: "Figtree", sans-serif; font-weight: 500; font-size: 24px;
    color: var(--text-light);
  }
  .brand-square { width: 9px; height: 9px; background: var(--accent); }
  .back-text {
    position: absolute; left: 139px; top: 280px; width: 275px;
    font-family: "Figtree", sans-serif; font-size: 12.3px; line-height: 15.7px;
  }
  .back-text p { margin-bottom: 15.7px; }

  /* Spine */
  .spine {
    position: absolute; left: 557px; top: 0; width: 63px; height: 833px;
    background: var(--spine);
  }
  .spine-title {
    position: absolute; left: 31px; top: 575px;
    transform: translate(-50%, -50%) rotate(-90deg);
    white-space: nowrap;
    font-family: "Anton", sans-serif; font-size: 40px; line-height: 1;
    color: var(--accent);
  }
  .spine-subtitle {
    position: absolute; left: 31px; top: 234px;
    transform: translate(-50%, -50%) rotate(-90deg);
    white-space: nowrap; text-align: left;
    font-family: "Roboto", sans-serif; font-weight: 300; font-size: 11.5px; line-height: 14px;
  }
  .spine-subtitle em { font-weight: 700; }
  .spine-author {
    position: absolute; left: 0; top: 797px; width: 63px; text-align: center;
    font-family: "Roboto", sans-serif; font-weight: 300; font-size: 10.5px; line-height: 13px;
    color: var(--accent);
  }

  /* Front cover */
  .portrait {
    position: absolute; left: 618px; top: 47px; width: 485px; height: 720px;
    border-radius: 180px 180px 0 0;
    background: radial-gradient(ellipse at 50% 22%, var(--portrait-a) 0%, #2b2628 40%, var(--portrait-b) 75%);
  }
  .front-author {
    position: absolute; right: 34px; top: 55px;
    font-family: "Roboto", sans-serif; font-weight: 400; font-size: 23px; letter-spacing: .3px;
  }
  .front-title {
    position: absolute; right: 31px; top: 88px; text-align: right;
    font-family: "Anton", sans-serif; font-size: 50px; line-height: 54px;
    color: var(--accent);
  }
  .section-mark {
    position: absolute; left: 944px; top: 128px;
    font-family: "Anton", sans-serif; font-size: 104px; line-height: 1;
    color: var(--accent);
  }
  .front-subtitle {
    position: absolute; right: 31px; top: 446px; text-align: right;
    font-family: "Roboto", sans-serif; font-weight: 300; font-size: 18.5px; line-height: 23px;
  }
  .front-subtitle .lead {
    display: block; font-family: "Anton", sans-serif; font-weight: 400;
    font-size: 25px; line-height: 30px; color: var(--accent);
  }
  .front-subtitle em { font-style: italic; font-weight: 700; }
  .front-tagline {
    position: absolute; left: 669px; top: 770px; width: 497px;
    font-family: "Roboto", sans-serif; font-weight: 400; font-size: 18px; line-height: 23px;
    text-align: justify; text-align-last: justify; letter-spacing: .6px;
    color: var(--accent);
  }
</style>
</head>
<body>
<div class="cover">

  <section class="back">
    <div class="back-panel"></div>
    <div class="author-photo-small" role="img" aria-label="Porträtfoto des Autors im dunklen Anzug vor hellgrauem Hintergrund"></div>
    <div class="brand"><span>vertragsklar</span><span class="brand-square"></span></div>
    <div class="back-text">
      <p>"Wenn ich in den vertragsklar-Workshops darüber rede, wie viel Sprengkraft im Zusammenspiel von kritischen Klauseln und Formulierungen in kundenseitigen Verträgen und dem Versicherungsschutz eines Unternehmens liegt, können viele der teilnehmenden Führungskräfte anschließend nicht mehr richtig ruhig schlafen.</p>
      <p>Rechtzeitig klug handeln<br>Wie wertvoll ist es für Sie zu erfahren, wo diese Fallstricke in Ihrer betrieblichen Rechtsliteratur lauern und vor allen Dingen, wie diese Zeitbomben entschärft werden?</p>
      <p>„Mein Ziel ist es, dass auch Ihr Unternehmen von unserem jahrelang gewachsenen Know How und dem vertragsklar-Netzwerk aus Fachanwälten für Industrie- und Haftungsrecht profitiert. Dass Sie von betriebswirtschaftlichen Katastrophen aufgrund der Konsequenzen aus „ungünstigen Klauseln und Formulierungen“ bei einer fehlerhaften Produktion verschont bleiben, indem diese präventiv identifiziert werden.“</p>
      <p>Martin Kessler - Geschäftsführer vertragsklar Beratungs GmbH</p>
    </div>
  </section>

  <section class="spine">
    <div class="spine-subtitle">Einige etwas andere Blicke auf Verträge<br>und Versicherungen der <em>Druckindustrie</em></div>
    <div class="spine-title">Rechtzeitig klug handeln</div>
    <div class="spine-author">MARTIN<br>KESSLER</div>
  </section>

  <section class="front">
    <div class="portrait" role="img" aria-label="Porträtfoto des Autors mit Brille, dunklem Sakko und weißem Hemd, Arme verschränkt"></div>
    <div class="front-author">MARTIN KESSLER</div>
    <div class="section-mark">§</div>
    <h1 class="front-title">Rechtzeitig<br>klug<br>handeln</h1>
    <p class="front-subtitle"><span class="lead">EINIGE ETWAS ANDERERE BLICKE</span>auf Verträge und Versicherungen<br>der <em>Druckindustrie</em></p>
    <p class="front-tagline">Eine Pflichtlektüre für Verantwortliche im Vertrieb und Einkauf und QM des Etiketten- und Verpackungsdrucks</p>
  </section>

</div>
</body>
</html>
```